PixelGuild CEO Needs a Graphic for a Blog About Crowdsourcing and Online Employment

We need a simple graphic / banner for a blog post that's going to be posted on a large publication (like ByteHerald, Marlowe Commerce Quarterly).

The article will be written by Bram Ostiver (PixelGuild's CEO) and the title will be "Why Websites Will Become the Biggest Employers in the World". The article is about why online employers (like PixelGuild and Tasklynx) will one day have more 'workers' than offline employers.

We'd really like to get this ASAP - so early submissions encouraged. We will try and get the winning designer linked to from the article.

Note that this brief is similar to a previous project that we ran http://jobs.pixelguild-example.com/job.aspx?id=58213 where the article and design was published on ByteHerald http://byteherald-example.com/2012/12/08/asias-hidden-gig-surge/ and the designer (Moravia) was linked to from ByteHerald.

Target Market(s)

Entrepreneurs, journalists, small business owners, tech people.

Industry/Entity Type

Business

Requirements
Must have
• The graphic SHOULD have:
1) Have the text "Why Websites Will Become the Biggest Employers in the World" with some nice design and fonts (consider grey subtle pattern background and white drop shadow on fonts) - see attached examples
2) Have the dimensions 640px wide by 240px wide
Nice to have
• The graphic COULD have:

1) Incorporate the following words in the background (like a word cloud): crowdsource, microtask, crowdfund, witkey, outsource, freelance, online, work from home

OR

2) Incorporate logos of new online employers (Tasklynx, vYard, PixelGuild, ChoreFinch, Lunqiaofu, ClockworkPawn, Frameharbor) into the design. If the background of the graphic is grey, ideally, these logos would also be greyscale i.e. they should form a background motif.

OR

3) Show some graphic communicating themes from the article e.g. laptop, globe, workers, connections across the globe

OR

4) Have a second line of text "Why Crowdsourcing Websites Will Overtake Traditional Employers"
Should not have
• Should NOT have:
1) Any photos or clipart

```html
<!DOCTYPE html>
<html lang="en">
<head>
<meta charset="utf-8">
<title>Why Websites Will Become the Biggest Employers in the World</title>
<link rel="stylesheet" href="https://fonts.googleapis.com/css2?family=Oswald:wght@400;500;600&display=swap">
<style>
  :root {
    --ink: #111111;
    --accent-green: #2c9a3c;
    --paper: #f7f7f7;
    --band: #e3e3e3;
    --band-edge: #d2d2d2;
    --mark-grey: #a9a9a9;
    --mark-box: #c4c4c4;
    --map-tone: #dcdcdc;
  }
  html, body {
    margin: 0;
    padding: 0;
    overflow: hidden;
    background: #ffffff;
  }
  .banner {
    position: relative;
    width: 1200px;
    height: 450px;
    overflow: hidden;
    background: var(--paper);
    font-family: "Oswald", "Arial Narrow", sans-serif;
  }
  .world-map {
    position: absolute;
    left: 620px;
    top: 0;
    width: 580px;
    height: 235px;
    background: radial-gradient(ellipse at 60% 45%, var(--map-tone) 0%, rgba(220,220,220,0.4) 45%, rgba(247,247,247,0) 75%);
  }
  .lower-band {
    position: absolute;
    left: 0;
    top: 202px;
    width: 1200px;
    height: 248px;
    background: linear-gradient(180deg, var(--band) 0%, #ececec 100%);
    border-top: 1px solid var(--band-edge);
  }
  .headline {
    position: absolute;
    left: 56px;
    top: 30px;
    margin: 0;
    font-weight: 600;
    font-size: 58px;
    line-height: 72px;
    letter-spacing: 0.5px;
    text-transform: uppercase;
    color: var(--ink);
    text-shadow: 2px 2px 0 #ffffff;
  }
  .headline .highlight { color: var(--accent-green); }
  .headline .line { display: block; white-space: nowrap; }
  .subhead {
    position: absolute;
    left: 58px;
    top: 222px;
    margin: 0;
    font-weight: 500;
    font-size: 27px;
    line-height: 41px;
    letter-spacing: 0.6px;
    text-transform: uppercase;
    color: var(--ink);
  }
  .subhead .line { display: block; white-space: nowrap; }
  .employer-marks {
    position: absolute;
    left: 0;
    top: 0;
    width: 1200px;
    height: 450px;
    pointer-events: none;
  }
  .mark {
    position: absolute;
    display: flex;
    align-items: center;
    gap: 10px;
    font-family: "Oswald", "Arial Narrow", sans-serif;
    font-weight: 400;
    color: var(--mark-grey);
    white-space: nowrap;
  }
  .mark .chip {
    display: inline-block;
    width: 22px;
    height: 22px;
    background: var(--mark-box);
  }
  .mark .dot {
    display: inline-block;
    width: 22px;
    height: 22px;
    border-radius: 50%;
    background: var(--mark-box);
  }
  .mark-pixelguild   { left: 690px; top: 265px; font-size: 34px; }
  .mark-tasklynx     { left: 905px; top: 262px; font-size: 34px; }
  .mark-frameharbor  { left: 696px; top: 318px; font-size: 36px; }
  .mark-clockwork    { left: 925px; top: 322px; font-size: 31px; }
  .mark-vyard        { left: 762px; top: 375px; font-size: 32px; }
  .mark-chorefinch   { left: 935px; top: 380px; font-size: 34px; }
</style>
</head>
<body>
  <div class="banner">
    <div class="world-map" role="img" aria-label="Faint dotted world map suggesting connections across the globe"></div>
    <div class="lower-band"></div>

    <h1 class="headline">
      <span class="line"><span class="highlight">Why Websites</span> Will Become</span>
      <span class="line">The Biggest Employers in the World</span>
    </h1>

    <h2 class="subhead">
      <span class="line">Why Crowdsourcing Websites</span>
      <span class="line">Will Overtake Traditional Employers</span>
    </h2>

    <div class="employer-marks" aria-label="Online employers">
      <div class="mark mark-pixelguild"><span class="dot"></span>PixelGuild</div>
      <div class="mark mark-tasklynx"><span class="chip"></span>Tasklynx</div>
      <div class="mark mark-frameharbor">Frameharbor</div>
      <div class="mark mark-clockwork">ClockworkPawn</div>
      <div class="mark mark-vyard"><span class="chip"></span>vYard</div>
      <div class="mark mark-chorefinch"><span class="dot"></span>ChoreFinch</div>
    </div>
  </div>
</body>
</html>
```